'Our Values' graphic

Hi there,
Could I get few options creating this graphic in a more minimalist, corporate look - using minimalist graphic elements and designs and using minimalist fonts (see google or freepik for inspiration)
I would also like the lines around the outside to be more minimalist. Maybe a thin line or a graphic element.
Change 'Core Values' title to 'Our Values'
Keep the font of 'Values'.
I would like to see a version in all dark grey and another version with the font in the lower square with each line of font being a different colour (Red, Blue, Green and Orange)

Requirements
Must have
• 'Our Values' and using the same font for 'Values' as the original artwork
Nice to have
• Minimalist artwork

```html
<!DOCTYPE html>
<html lang="en">
<head>
<meta charset="utf-8">
<title>Our Values</title>
<link rel="stylesheet" href="https://fonts.googleapis.com/css2?family=Montserrat:wght@800&family=Gochi+Hand&display=swap">
<style>
  :root {
    --bg: #d3d4d6;
    --frame: #3a3a3c;
    --charcoal: #454545;
    --sky: #00aeef;
    --white: #ffffff;
    --red: #ec2a32;
    --blue: #00aeef;
    --green: #0aa04b;
    --orange: #f58a2a;
  }
  html, body { margin: 0; padding: 0; overflow: hidden; }
  body { width: 1200px; height: 1005px; background: var(--bg); }
  .values-board { display: block; width: 1200px; height: 1005px; }
  .frame { fill: none; stroke: var(--frame); stroke-width: 1.2; }
  .title-our { font-family: 'Montserrat', sans-serif; font-weight: 800; font-size: 112px; fill: var(--white); letter-spacing: -2px; }
  .title-values { font-family: 'Gochi Hand', cursive; font-size: 100px; fill: var(--white); stroke: var(--white); stroke-width: 1.5; }
  .value-item { font-family: 'Gochi Hand', cursive; font-size: 36px; letter-spacing: -1px; }
  .dark .value-item { fill: var(--white); }
  .light .value-item { font-size: 33px; }
  .c-red { fill: var(--red); } .c-blue { fill: var(--blue); }
  .c-green { fill: var(--green); } .c-orange { fill: var(--orange); }
</style>
</head>
<body>
<svg class="values-board" viewBox="0 0 1200 1005" xmlns="http://www.w3.org/2000/svg">
  <!-- Dark version -->
  <g class="card dark">
    <rect class="frame" x="172" y="295" width="414" height="415" rx="26"/>
    <rect x="179" y="302" width="402" height="402" rx="22" fill="var(--charcoal)"/>
    <text class="title-our" x="379" y="420" text-anchor="middle">OUR</text>
    <text class="title-values" x="400" y="474" text-anchor="middle">Values</text>
    <text class="value-item" x="379" y="544" text-anchor="middle">◦ RISE TOGETHER</text>
    <text class="value-item" x="379" y="591" text-anchor="middle">◦ INNOVATE EDUCATION</text>
    <text class="value-item" x="379" y="637" text-anchor="middle">◦ SAFETY FIRST</text>
    <text class="value-item" x="379" y="683" text-anchor="middle">◦ EMPOWER CONNECTIONS</text>
  </g>
  <!-- Colour version -->
  <g class="card light">
    <rect class="frame" x="613" y="295" width="414" height="415" rx="26"/>
    <rect x="619" y="302" width="403" height="402" rx="22" fill="var(--white)"/>
    <path d="M619 526 V324 a22 22 0 0 1 22 -22 H1000 a22 22 0 0 1 22 22 V526 Z" fill="var(--sky)"/>
    <text class="title-our" x="820" y="420" text-anchor="middle">OUR</text>
    <text class="title-values" x="841" y="474" text-anchor="middle">Values</text>
    <text class="value-item c-red" x="825" y="560" text-anchor="middle">◦ RISE TOGETHER</text>
    <text class="value-item c-blue" x="825" y="602" text-anchor="middle">◦ INNOVATE EDUCATION</text>
    <text class="value-item c-green" x="825" y="643" text-anchor="middle">◦ SAFETY FIRST</text>
    <text class="value-item c-orange" x="825" y="685" text-anchor="middle">◦ EMPOWER CONNECTIONS</text>
  </g>
</svg>
</body>
</html>
```